Contractor Business Card Design

Looking to have a card made that has a bold description of (KITCHENS, BASEMENTS, BATHROOMS)

Definition and layers a plus

Contact info is;

Mark T. Ellery
Brookhaven, MN 55012
Cell: 612-555-0147
website: www.cobaltfinishworks.example
Email: cobaltfinishworksmn@mailbox.example

colors: red, black, gray, white

Contact Information for Business Card

Contact info is;

Mark T. Ellery
Brookhaven, MN 55012
Cell: 612-555-0147

Colors
ec1f27

Requirements
Must have
• Looking for layers and definition
Nice to have
• Cards are planned to be printed on plastic cards

```html
<!DOCTYPE html>
<html lang="en">
<head>
<meta charset="utf-8">
<title>Cobalt Finish Works – Business Card</title>
<link rel="stylesheet" href="https://fonts.googleapis.com/css2?family=Montserrat:wght@300;400;500;600;700&display=swap">
<style>
  :root {
    --red: #ec1f27;
    --deep-red: #b3161c;
    --black: #0b0b0b;
    --charcoal: #2b2b2b;
    --gray: #c9c9c9;
    --light-gray: #9a9a9a;
    --white: #ffffff;
    --frost-a: #f4f2ef;
    --frost-b: #dcd8d3;
    --backdrop: #d8d3cb;
  }
  * { margin: 0; padding: 0; box-sizing: border-box; }
  html, body {
    width: 1200px; height: 969px; overflow: hidden;
    background: var(--backdrop);
    font-family: "Montserrat", sans-serif;
  }
  .card {
    position: absolute; left: 152px; top: 226px;
    width: 936px; height: 534px;
    border-radius: 34px; overflow: hidden;
    background: linear-gradient(160deg, var(--frost-a), var(--frost-b));
    box-shadow: 0 18px 40px rgba(0,0,0,0.25);
  }
  .card-shapes { position: absolute; inset: 0; }
  .brand {
    position: absolute; left: 70px; top: 80px; width: 260px;
    text-align: center; color: var(--charcoal); font-weight: 700;
  }
  .brand-dot {
    display: block; width: 144px; height: 144px; margin: 0 auto 26px;
    border: 5px solid var(--red); border-radius: 50%;
  }
  .brand-name { font-size: 50px; line-height: 1; letter-spacing: 1px; }
  .brand-sub { font-size: 17px; letter-spacing: 8px; margin-top: 10px; }
  .contact {
    position: absolute; right: 72px; top: 192px;
    text-align: right; color: var(--gray);
  }
  .contact-name {
    font-weight: 700; font-size: 29px; line-height: 36px; color: var(--deep-red);
  }
  .contact-role {
    font-weight: 600; font-size: 19px; line-height: 24px; color: var(--white);
  }
  .contact-lines { margin-top: 16px; font-size: 19px; line-height: 27px; }
  .contact-lines .email { font-weight: 300; font-size: 18px; }
  .contact-lines .web { font-weight: 300; font-size: 18px; color: var(--light-gray); }
  .services { list-style: none; margin-top: 16px; }
  .services li {
    font-size: 20px; line-height: 27px; color: var(--gray);
    display: flex; justify-content: flex-end; align-items: center; gap: 12px;
  }
  .services svg { width: 18px; height: 18px; }
</style>
</head>
<body>
  <div class="card">
    <svg class="card-shapes" viewBox="0 0 936 534" width="936" height="534">
      <path d="M660 0 C590 10 560 110 508 240 C460 360 410 480 330 534 L300 534 C390 480 445 360 495 240 C548 110 580 10 640 0 Z" fill="var(--deep-red)"/>
      <path d="M684 0 L936 0 L936 534 L300 534 C400 500 470 380 522 250 C572 125 605 12 684 0 Z" fill="var(--black)"/>
    </svg>

    <div class="brand">
      <span class="brand-dot"></span>
      <p class="brand-name">COBALT</p>
      <p class="brand-sub">FINISH WORKS</p>
    </div>

    <div class="contact">
      <p class="contact-name">MARK T. ELLERY</p>
      <p class="contact-role">President</p>
      <div class="contact-lines">
        <p>Brookhaven, MN 55012</p>
        <p>612-555-0147</p>
        <p class="email">cobaltfinishworksmn@mailbox.example</p>
        <p class="web">www.cobaltfinishworks.example</p>
      </div>
      <ul class="services">
        <li>KITCHENS <svg viewBox="0 0 18 18"><rect x="1" y="2" width="15" height="15" fill="none" stroke="var(--red)" stroke-width="1.6"/><path d="M4 9 L8 13 L17 2" fill="none" stroke="var(--red)" stroke-width="1.8"/></svg></li>
        <li>BASEMENTS <svg viewBox="0 0 18 18"><rect x="1" y="2" width="15" height="15" fill="none" stroke="var(--red)" stroke-width="1.6"/><path d="M4 9 L8 13 L17 2" fill="none" stroke="var(--red)" stroke-width="1.8"/></svg></li>
        <li>BATHROOMS <svg viewBox="0 0 18 18"><rect x="1" y="2" width="15" height="15" fill="none" stroke="var(--red)" stroke-width="1.6"/><path d="M4 9 L8 13 L17 2" fill="none" stroke="var(--red)" stroke-width="1.8"/></svg></li>
      </ul>
    </div>
  </div>
</body>
</html>
```